Postcard Design Project A Healthy reminder

Dr.'s Jeetesh and Lorna sethi. Internal Medicine/Family practice. This postcard will be for our patients that we have not seen in a while. Also we need another postcard (the one your designing) with a different heading for New patient's. Do you offer a price break for that? The only thing we would need to change is the heading. Please let me know. Thank you so much! Also can you use the map on the last postcard and our logo I made? I cant find it. Please feel free to call me or email me.

```html
<!DOCTYPE html>
<html lang="en">
<head>
<meta charset="utf-8">
<title>Jeetesh T. Sethi, M.D. – New Patient Postcard</title>
<link rel="stylesheet" href="https://fonts.googleapis.com/css2?family=Oswald:wght@500;600&family=Fira+Sans:wght@500;600&family=Lato:wght@400;700&display=swap">
<style>
  :root {
    --red: #cc1f27;
    --black: #0b0b0b;
    --ink: #1a1a1a;
    --white: #ffffff;
    --panel: #efefef;
    --backdrop: #5e5e5e;
    --stamp: #ececec;
    --photo-light: #e3d6ca;
    --photo-mid: #b79e8a;
    --photo-dark: #6e5849;
    --map-light: #f4f1ea;
    --map-mid: #e6e0cf;
  }
  * { box-sizing: border-box; margin: 0; padding: 0; }
  html, body {
    width: 1200px; height: 1200px; overflow: hidden;
    background: var(--backdrop);
    font-family: "Lato", Arial, sans-serif;
  }
  .canvas { position: relative; width: 1200px; height: 1200px; }

  .postcard { position: absolute; overflow: hidden; background: var(--white); }
  .postcard--front { left: 68px; top: 86px; width: 698px; height: 476px; }
  .postcard--back  { left: 425px; top: 631px; width: 707px; height: 482px; }

  .front-art { position: absolute; left: 0; top: 0; width: 698px; height: 300px; }

  .practice-name {
    position: absolute; text-align: center;
    font-family: "Lato", Arial, sans-serif; font-weight: 700;
    color: var(--ink); white-space: nowrap;
  }
  .practice-tagline {
    position: absolute; text-align: center;
    font-family: "Lato", Arial, sans-serif; font-weight: 700;
    color: var(--ink); letter-spacing: 1px; white-space: nowrap;
  }
  .postcard--front .practice-name { left: 56px; width: 142px; top: 328px; font-size: 14px; }
  .postcard--front .practice-tagline { left: 56px; width: 142px; top: 385px; font-size: 7px; }

  .headline {
    position: absolute; left: 264px; top: 300px;
    font-family: "Oswald", "Arial Narrow", sans-serif; font-weight: 600;
    font-size: 46px; line-height: 52px; color: var(--red);
    white-space: nowrap;
    transform: scaleX(0.86); transform-origin: left top;
  }

  .contact-bar {
    position: absolute; left: 0; top: 402px; width: 698px; height: 54px;
    background: var(--black); color: var(--white);
  }
  .accent-bar { position: absolute; left: 0; top: 456px; width: 698px; height: 20px; background: var(--red); }

  .contact-item { position: absolute; display: flex; align-items: flex-start; gap: 8px; white-space: nowrap; }
  .contact-item svg { flex: none; }
  .contact-item--phone { left: 26px; top: 13px; font-size: 18px; }
  .contact-item--address { left: 204px; top: 14px; font-size: 15px; line-height: 19px; }
  .contact-item--web { left: 458px; top: 14px; font-size: 15px; }

  .mission-panel { position: absolute; left: 0; top: 0; width: 707px; height: 482px; }
  .mission-title {
    position: absolute; left: 26px; top: 22px;
    font-family: "Fira Sans", Arial, sans-serif; font-weight: 600;
    font-size: 34px; color: var(--red);
  }
  .mission-copy {
    position: absolute; left: 26px; top: 67px; width: 322px;
    font-size: 12.2px; line-height: 15.2px; color: var(--ink);
  }
  .mission-copy p + p { margin-top: 15px; }
  .call-button {
    position: absolute; left: 26px; top: 311px; width: 190px; height: 35px;
    border-radius: 18px; background: var(--red); color: var(--white);
    display: flex; align-items: center; justify-content: center; gap: 8px; font-size: 17px;
  }
  .back-contact { position: absolute; color: var(--white); display: flex; gap: 8px; align-items: flex-start; white-space: nowrap; }
  .back-contact--address { left: 26px; top: 362px; font-size: 15px; line-height: 19px; }
  .back-contact--web { left: 26px; top: 406px; font-size: 15px; }
  .social-note { position: absolute; left: 29px; top: 434px; font-size: 12px; color: var(--white); }

  .postcard--back .practice-name { left: 392px; width: 128px; top: 68px; font-size: 12px; }
  .postcard--back .practice-tagline { left: 392px; width: 128px; top: 114px; font-size: 6px; }

  .stamp-box { position: absolute; left: 605px; top: 28px; width: 72px; height: 81px; background: var(--stamp); }
  .address-line { position: absolute; left: 510px; width: 170px; height: 2px; background: var(--black); }
</style>
</head>
<body>
<div class="canvas">

  <section class="postcard postcard--front">
    <svg class="front-art" viewBox="0 0 698 300" width="698" height="300">
      <defs>
        <linearGradient id="photoTone" x1="0" y1="0" x2="1" y2="1">
          <stop offset="0" stop-color="var(--photo-light)"/>
          <stop offset="0.5" stop-color="var(--photo-mid)"/>
          <stop offset="1" stop-color="var(--photo-dark)"/>
        </linearGradient>
      </defs>
      <path role="img" aria-label="Photo of two doctors in white coats reviewing a patient chart in a clinic hallway"
            d="M0 0 H698 V178 C600 250 450 268 300 262 C180 258 80 250 0 255 Z" fill="url(#photoTone)"/>
      <path d="M0 255 C80 250 180 258 300 262 C450 268 600 250 698 178 V250 C600 292 450 290 300 282 C180 276 80 266 0 270 Z" fill="var(--black)"/>
      <path d="M0 268 C100 262 200 272 300 280 C420 290 520 290 620 276 C520 302 400 302 300 294 C180 286 80 280 0 286 Z" fill="var(--red)"/>
    </svg>

    <div class="practice-name">Jeetesh T. Sethi, M.D.</div>
    <div class="practice-tagline">A Primary Care Office</div>

    <h1 class="headline">Now welcoming<br>new patients!</h1>

    <div class="contact-bar">
      <div class="contact-item contact-item--phone">
        <svg width="16" height="16" viewBox="0 0 24 24" style="margin-top:4px"><circle cx="12" cy="12" r="10.5" fill="none" stroke="var(--red)" stroke-width="2"/><path d="M8.5 7 L10.5 7 L11.2 9.6 L10 10.6 C10.6 12 11.8 13.3 13.4 14 L14.4 12.8 L17 13.5 L17 15.5 C12 16 8 12 8.5 7 Z" fill="var(--red)"/></svg>
        <span>(555) 014-2280</span>
      </div>
      <div class="contact-item contact-item--address">
        <svg width="14" height="19" viewBox="0 0 14 19"><path d="M7 0 C3 0 0 3 0 7 C0 12 7 19 7 19 C7 19 14 12 14 7 C14 3 11 0 7 0 Z" fill="var(--red)"/><circle cx="7" cy="7" r="2.6" fill="var(--black)"/></svg>
        <span>2480 N. Alder Street Suite 204<br>Cedarvale, Ca 90014</span>
      </div>
      <div class="contact-item contact-item--web">
        <svg width="15" height="15" viewBox="0 0 24 24" style="margin-top:2px"><g fill="none" stroke="var(--red)" stroke-width="2"><circle cx="12" cy="12" r="10"/><ellipse cx="12" cy="12" rx="4.5" ry="10"/><path d="M2 12 H22 M4 6.5 H20 M4 17.5 H20"/></g></svg>
        <span>www.jeeteshtsethimd.com</span>
      </div>
    </div>
    <div class="accent-bar"></div>
  </section>

  <section class="postcard postcard--back">
    <svg class="mission-panel" viewBox="0 0 707 482" width="707" height="482">
      <defs>
        <radialGradient id="mapTone" cx="0.5" cy="0.5" r="0.5">
          <stop offset="0" stop-color="var(--map-light)"/>
          <stop offset="1" stop-color="var(--map-mid)"/>
        </radialGradient>
      </defs>
      <path d="M0 0 H392 C368 120 380 200 390 300 C398 380 380 440 365 482 H0 Z" fill="var(--panel)"/>
      <path d="M0 355 H394 C396 410 382 450 365 482 H0 Z" fill="var(--black)"/>
      <path d="M392 0 C368 120 380 200 390 300 C398 380 380 440 365 482" fill="none" stroke="var(--red)" stroke-width="5"/>
      <circle cx="351" cy="329" r="70" fill="var(--white)"/>
      <circle role="img" aria-label="Street map of the city area with a pin marking the office location"
              cx="351" cy="329" r="62" fill="url(#mapTone)"/>
      <circle cx="351" cy="329" r="69" fill="none" stroke="var(--red)" stroke-width="3"/>
    </svg>

    <h2 class="mission-title">Our Mission</h2>
    <div class="mission-copy">
      <p>Our office is committed to working with each individual patient to achieve and maintain their optimal wellbeing. We strive to deliver high quality, compassionate care. We are committed to offering affordable medical services to patients in an atmosphere of respect, professionalism and confidentiality.</p>
      <p>Our Physicians and healthcare staff are dedicated to providing thorough, informative healthcare. We promise our patients to keep them up to date, educated, and informed. We are confident our care is of the utmost quality, and the needs of our patients will always be our first priority.</p>
      <p>We look forward to working together closely<br>towards a healthier future</p>
    </div>

    <div class="call-button">
      <svg width="16" height="16" viewBox="0 0 24 24"><circle cx="12" cy="12" r="10.5" fill="none" stroke="var(--white)" stroke-width="2"/><path d="M8.5 7 L10.5 7 L11.2 9.6 L10 10.6 C10.6 12 11.8 13.3 13.4 14 L14.4 12.8 L17 13.5 L17 15.5 C12 16 8 12 8.5 7 Z" fill="var(--white)"/></svg>
      <span>(555) 014-2280</span>
    </div>

    <div class="back-contact back-contact--address">
      <svg width="12" height="17" viewBox="0 0 14 19" style="margin-top:2px"><path d="M7 0 C3 0 0 3 0 7 C0 12 7 19 7 19 C7 19 14 12 14 7 C14 3 11 0 7 0 Z" fill="var(--red)"/><circle cx="7" cy="7" r="2.6" fill="var(--black)"/></svg>
      <span>2480 N. Alder Street Suite 204<br>Cedarvale, Ca 90014</span>
    </div>
    <div class="back-contact back-contact--web">
      <svg width="14" height="14" viewBox="0 0 24 24" style="margin-top:3px"><g fill="none" stroke="var(--red)" stroke-width="2"><circle cx="12" cy="12" r="10"/><ellipse cx="12" cy="12" rx="4.5" ry="10"/><path d="M2 12 H22 M4 6.5 H20 M4 17.5 H20"/></g></svg>
      <span>www.jeeteshtsethimd.com</span>
    </div>
    <div class="social-note">visit us on social media</div>

    <div class="practice-name">Jeetesh T. Sethi, M.D.</div>
    <div class="practice-tagline">A Primary Care Office</div>

    <div class="stamp-box"></div>
    <div class="address-line" style="top:211px"></div>
    <div class="address-line" style="top:245px"></div>
    <div class="address-line" style="top:279px"></div>
  </section>

</div>
</body>
</html>
```